Label for Velmor Equine Chia-based Pellets

Design for the front and back labels of an equine supplement that will be sold in a resealable bag. This supplement has been developed using chia, a well-known super-food that is consumed by health-conscious humans and also performance horses. Consuming chia is known to have several benefits for horses and these are highlighted in the uploaded file. Although the benefits of chia for horses are well-known, pure chia is very expensive, which limits consumption. We have combined chia with other traditional horse feeds (oats, sunflower seed, pumpkin seed and sesame seed) to create a healthy, 100% natural supplement for horses that is reasonably-priced. The product is highly palatable and minimally processed, preserving its natural attributes.

Target Market(s)

Owners of competition horses who wish to maximize their health, performance and appearance.

Industry/Entity Type

Supplement

Font styles to use
Sans Serif

Colors
cadf82
33b8a4

Requirements
Must have
• Highlight that the product is based on chia.
• Highlight that the product includes traditional horse feeds (oats, sunflower, pumpkin and sesame seeds)
• Must give the impression of vitality, well-being and contentment. Must make the owner feel she/he is investing in her/his horse's health.
Nice to have
• Nice to related the mythical name (Velmor) to the benefits the owner wants to grant the horse.
Should not have
• Exaggerated promises.

```html
<!DOCTYPE html>
<html lang="en">
<head>
<meta charset="utf-8">
<title>Velmor General Supplement Soft Pellets – Label</title>
<link href="https://fonts.googleapis.com/css2?family=Cinzel:wght@500&family=Oswald:wght@500&family=Open+Sans:wght@700;800&family=Roboto+Condensed:wght@400&display=swap" rel="stylesheet">
<style>
  :root {
    --page: #ececec;
    --band: #1f3d14;
    --band-deep: #16300f;
    --sky-top: #a9c6d6;
    --sky-low: #d9e3e4;
    --field: #4f8a32;
    --field-dark: #2f5c1e;
    --seed: #b8bcc0;
    --title-yellow: #f2e64a;
    --label-green: #a4dc6a;
    --tag-yellow: #f5ea3b;
    --white: #ffffff;
    --brand-brown: #4a3a1e;
    --row-dark: #0f1f0a;
  }
  * { box-sizing: border-box; margin: 0; padding: 0; }
  html, body { width: 969px; height: 1200px; overflow: hidden; background: var(--page); }
  .label { position: relative; width: 969px; height: 1200px; }

  .panel { position: absolute; top: 40px; height: 1120px; overflow: hidden; }
  .panel--front { left: 20px; width: 610px; }
  .panel--side { left: 640px; width: 309px; background: var(--band); }

  .scene {
    position: absolute; inset: 0;
    background: linear-gradient(180deg, var(--sky-top) 0%, var(--sky-low) 24%, #9bb48a 30%, var(--field) 38%, var(--field-dark) 62%, #6b5a44 74%, var(--seed) 86%, #9fa3a6 100%);
  }

  .front-band {
    position: absolute; left: 150px; top: 0; width: 240px; height: 100%;
    background: linear-gradient(180deg, rgba(31,61,20,.95), rgba(22,48,15,.9));
  }

  .brand {
    position: absolute; left: 14px; right: 14px; top: 0; height: 215px;
    background: var(--white); border-radius: 0 0 26px 26px;
    display: flex; flex-direction: column; align-items: center; justify-content: center; gap: 14px;
  }
  .brand__dot { width: 70px; height: 70px; border-radius: 50%; background: #d8c9a4; }
  .brand__name { font-family: "Cinzel", serif; font-weight: 500; font-size: 30px; color: var(--brand-brown); letter-spacing: 1px; }

  .product-name {
    font-family: "Cinzel", serif; font-weight: 500; color: var(--title-yellow);
    text-align: center; line-height: 1;
  }
  .product-type {
    font-family: "Oswald", sans-serif; font-weight: 500; color: var(--label-green);
    text-align: center; line-height: 1.15;
  }

  .front-band .product-name { position: absolute; top: 245px; left: 0; right: 0; font-size: 50px; }
  .front-band .product-type { position: absolute; top: 310px; left: 0; right: 0; font-size: 36px; }

  .story {
    position: absolute; top: 470px; left: 16px; right: 8px;
    font-family: "Open Sans", sans-serif; font-weight: 700; font-size: 14.5px; line-height: 1.48;
    color: var(--white);
  }

  .ingredients { position: absolute; top: 705px; left: 0; right: -90px; list-style: none; }
  .ingredients li { display: flex; align-items: center; height: 58px; }
  .ingredient__swatch { width: 48px; height: 48px; border-radius: 50%; border: 3px solid #4fbf3c; flex: none; }
  .ingredient__name {
    margin-left: 20px; font-family: "Open Sans", sans-serif; font-weight: 800; font-size: 16px; color: var(--tag-yellow);
  }
  .tagline {
    position: absolute; top: 940px; left: 0; right: -40px;
    font-family: "Oswald", sans-serif; font-weight: 500; font-size: 30px; color: var(--label-green); text-align: center;
  }

  .net-weight {
    position: absolute; left: 412px; top: 955px;
    font-family: "Open Sans", sans-serif; font-weight: 800; font-size: 17px; line-height: 1.15; color: var(--tag-yellow);
  }

  .panel--side .brand { left: 36px; right: 36px; height: 205px; }
  .panel--side .product-name { margin-top: 250px; font-size: 46px; }
  .panel--side .product-type { margin-top: 10px; font-size: 30px; }

  .analysis { margin: 20px 12px 0; font-family: "Roboto Condensed", sans-serif; font-size: 10.5px; color: var(--white); }
  .analysis__meta { line-height: 1.7; }
  .analysis table { width: 100%; border-collapse: collapse; margin-top: 6px; }
  .analysis th { font-weight: 400; text-align: left; padding-bottom: 4px; }
  .analysis td { padding: 3px 4px; }
  .analysis tbody tr:nth-child(odd) { background: var(--row-dark); }
  .analysis .num { text-align: center; }
</style>
</head>
<body>
<main class="label">

  <section class="panel panel--front">
    <div class="scene" role="img" aria-label="Photo of chestnut horses galloping through a green chia field under hills, with chia seeds scattered across the lower area"></div>

    <div class="front-band">
      <header class="brand">
        <span class="brand__dot"></span>
        <span class="brand__name">SOLENNE</span>
      </header>

      <h1 class="product-name">VELMOR</h1>
      <p class="product-type">General<br>Supplement<br>Soft Pellets</p>

      <p class="story">Velmor was an extremely swift and immortal mythological horse. This general application supplement is based on chia and promotes several benefits similar to those enjoyed by the original Velmor. It is recommended for horses of any age.</p>

      <ul class="ingredients">
        <li><span class="ingredient__swatch" role="img" aria-label="Oats" style="background:#d9c79a"></span><span class="ingredient__name">+ plus oats</span></li>
        <li><span class="ingredient__swatch" role="img" aria-label="Sunflower seeds" style="background:#4a4a44"></span><span class="ingredient__name">+ sunflower seeds</span></li>
        <li><span class="ingredient__swatch" role="img" aria-label="Pumpkin seeds" style="background:#8a8a4e"></span><span class="ingredient__name">+ pumpkin seeds</span></li>
        <li><span class="ingredient__swatch" role="img" aria-label="Sesame seeds" style="background:#d8b880"></span><span class="ingredient__name">+ sesame seeds</span></li>
      </ul>

      <p class="tagline">Perfect balance</p>
    </div>

    <p class="net-weight">Net Weight:<br>10 lb. (4.45 kg)<br>30 servings</p>
  </section>

  <section class="panel panel--side">
    <header class="brand">
      <span class="brand__dot"></span>
      <span class="brand__name">SOLENNE</span>
    </header>

    <h2 class="product-name">VELMOR</h2>
    <p class="product-type">General<br>Supplement<br>Soft Pellets</p>

    <div class="analysis">
      <p class="analysis__meta">Guaranteed Analysis<br>Serving Size: 1 scoop (2 oz.)</p>
      <table>
        <thead>
          <tr><th></th><th class="num">Concentration</th><th class="num">Per 2 oz. Scoop</th><th class="num">% Daily Need*</th></tr>
        </thead>
        <tbody>
          <tr><td>Crude Protein</td><td class="num">xx%</td><td class="num">2 mg</td><td class="num">20%</td></tr>
          <tr><td>Crude Fat</td><td class="num">xx%</td><td class="num">2 mg</td><td class="num">20%</td></tr>
          <tr><td>Crude Fiber</td><td class="num">xx%</td><td class="num">2 mg</td><td class="num">20%</td></tr>
          <tr><td>Calcium (min)</td><td class="num">xx%</td><td class="num">2 mg</td><td class="num">20%</td></tr>
          <tr><td>Calcium (max)</td><td class="num">xx%</td><td class="num">2 mg</td><td class="num">20%</td></tr>
          <tr><td>Phosphorus</td><td class="num">xx%</td><td class="num">2 mg</td><td class="num">20%</td></tr>
          <tr><td>Sodium (min)</td><td class="num">xx%</td><td class="num">2 mg</td><td class="num">20%</td></tr>
          <tr><td>Sodium (max)</td><td class="num">xx%</td><td class="num">2 mg</td><td class="num">20%</td></tr>
          <tr><td>Copper</td><td class="num">xx%</td><td class="num">2 mg</td><td class="num">20%</td></tr>
          <tr><td>Selenium (min)</td><td class="num">xx%</td><td class="num">2 mg</td><td class="num">20%</td></tr>
          <tr><td>Selenium (max)</td><td class="num">xx%</td><td class="num">2 mg</td><td class="num">20%</td></tr>
          <tr><td>Zinc</td><td class="num">xx%</td><td class="num">2 mg</td><td class="num">20%</td></tr>
          <tr><td>Vitamin A</td><td class="num">xx%</td><td class="num">2 mg</td><td class="num">20%</td></tr>
          <tr><td>Magnesium</td><td class="num">xx%</td><td class="num">2 mg</td><td class="num">20%</td></tr>
          <tr><td>Potassium</td><td class="num">xx%</td><td class="num">2 mg</td><td class="num">20%</td></tr>
          <tr><td>Iron</td><td class="num">xx%</td><td class="num">2 mg</td><td class="num">20%</td></tr>
          <tr><td>Manganese</td><td class="num">xx%</td><td class="num">2 mg</td><td class="num">20%</td></tr>
          <tr><td>Cobalt</td><td class="num">xx%</td><td class="num">2 mg</td><td class="num">20%</td></tr>
          <tr><td>Iodine</td><td class="num">xx%</td><td class="num">2 mg</td><td class="num">20%</td></tr>
          <tr><td>Vitamin D</td><td class="num">xx%</td><td class="num">2 mg</td><td class="num">20%</td></tr>
          <tr><td>Vitamin E</td><td class="num">xx%</td><td class="num">2 mg</td><td class="num">20%</td></tr>
        </tbody>
      </table>
    </div>
  </section>

</main>
</body>
</html>
```